Social Media Card

We would like a social media card to hand out to our customers.
It should be double sided, with the front to say in bold letters Follow Us!
We would like the card to be two toned in our brand colors (espresso brown & copper.) I still want a modern, clean look to the card but it can be a bit more "fun" than our business cards. I have attached the previous card that you did but you don't have to stick to the brown background/copper lettering as shown.
The font is josefin. We would need our logo either on the front or the back side.
I think I want social media icons but not the same old boring ones.
Our social media information is as follows:
Facebook: Vandell Jewelry
Twitter: Vandell Jewelry
Pinterest: vkbtqm
Instagram: Vandell Jewelry
Looking forward to seeing what you come up with!
Thanks!
Nell

Our address, etc info will need to be added.

Lakemoor Court # 7

Brookfern Plaza

Londonderry, NH 03999

(603)555-0187

www.vandelljewelry.example

info@vandelljewelry.example

```html
<!DOCTYPE html>
<html lang="en">
<head>
<meta charset="utf-8">
<title>Vandell Jewelry – Social Media Card</title>
<link rel="stylesheet" href="https://fonts.googleapis.com/css2?family=Josefin+Sans:wght@300;400&family=Open+Sans:wght@400;500&display=swap">
<style>
  :root {
    --espresso: #2a1811;
    --copper: #c4651f;
    --copper-dim: #a9581d;
    --band: #6e3c19;
    --icon-ghost: #8a4a1c;
    --stage: #e9e8ec;
  }
  * { box-sizing: border-box; margin: 0; padding: 0; }
  html, body {
    width: 1200px; height: 900px; overflow: hidden;
    background: var(--stage);
  }
  .canvas { position: relative; width: 1200px; height: 900px; }

  .card {
    position: absolute; top: 296px;
    width: 540px; height: 309px;
    background: var(--espresso);
    box-shadow: 0 4px 14px rgba(0,0,0,.25);
    overflow: hidden;
  }
  .card--front { left: 40px; }
  .card--back  { left: 620px; }

  /* front */
  .follow-pill {
    position: absolute; left: 153px; top: 83px;
    width: 275px; height: 106px; border-radius: 53px;
    background: var(--copper);
    display: flex; align-items: center; justify-content: center;
    font-family: "Open Sans", sans-serif; font-weight: 500;
    font-size: 50px; letter-spacing: -1px; color: var(--espresso);
  }
  .pointer-icon {
    position: absolute; left: 92px; top: 138px;
    width: 50px; height: 44px; border-radius: 10px;
    background: var(--copper-dim); opacity: .55;
  }
  .brand {
    font-family: "Josefin Sans", sans-serif; color: var(--copper-dim);
  }
  .brand__name { font-weight: 300; font-size: 34px; letter-spacing: 1px; line-height: 1; }
  .brand__tag  { font-weight: 300; font-size: 11.5px; letter-spacing: .3px; margin-top: 2px; }
  .card--front .brand { position: absolute; right: 34px; top: 226px; text-align: left; }

  /* back */
  .browser-bar {
    position: absolute; left: 0; top: 0; width: 100%; height: 80px;
    background: var(--band);
  }
  .browser-bar__nav {
    position: absolute; left: 12px; top: 34px;
  }
  .search-field {
    position: absolute; left: 136px; top: 22px;
    width: 384px; height: 44px; border-radius: 14px;
    background: var(--copper);
    display: flex; align-items: center;
    font-family: "Open Sans", sans-serif; font-size: 18px; color: var(--band);
  }
  .search-field svg { margin: 0 18px 0 12px; }
  .card--back .brand { position: absolute; left: 0; width: 100%; top: 128px; text-align: center; }
  .social-list {
    position: absolute; left: 47px; top: 245px;
    display: flex; align-items: center; list-style: none;
  }
  .social-list li {
    display: flex; align-items: center; gap: 7px;
    font-family: "Open Sans", sans-serif; font-size: 10.5px; color: var(--copper-dim);
    margin-right: 22px;
  }
  .social-list li:last-child { margin-right: 0; }
  .social-dot {
    width: 32px; height: 32px; border-radius: 50%;
    background: var(--icon-ghost);
  }
</style>
</head>
<body>
<main class="canvas">

  <section class="card card--front" aria-label="Card front">
    <div class="pointer-icon" role="img" aria-label="Pointing hand icon"></div>
    <div class="follow-pill">follow us</div>
    <div class="brand">
      <div class="brand__name">vandell</div>
      <div class="brand__tag">Jewelry &amp; Design Studio</div>
    </div>
  </section>

  <section class="card card--back" aria-label="Card back">
    <div class="browser-bar">
      <svg class="browser-bar__nav" width="104" height="20" viewBox="0 0 104 20" fill="none" stroke="#a9581d" stroke-width="2" stroke-linecap="round" stroke-linejoin="round" aria-hidden="true">
        <path d="M18 10H2M8 4L2 10l6 6"/>
        <path d="M40 10h16M50 4l6 6-6 6"/>
        <path d="M92 4a7 7 0 1 0 6 4"/>
        <path d="M99 2v6h-6"/>
      </svg>
      <div class="search-field">
        <svg width="26" height="26" viewBox="0 0 26 26" aria-hidden="true">
          <circle cx="10" cy="10" r="7" fill="none" stroke="#6e3c19" stroke-width="3"/>
          <path d="M15 15l8 8" stroke="#6e3c19" stroke-width="4.5" stroke-linecap="round"/>
        </svg>
        www.vandelljewelry.example
      </div>
    </div>
    <div class="brand">
      <div class="brand__name">vandell</div>
      <div class="brand__tag">Jewelry &amp; Design Studio</div>
    </div>
    <ul class="social-list">
      <li><span class="social-dot"></span>Vandell Jewelry</li>
      <li><span class="social-dot"></span>Vandell Jewelry</li>
      <li><span class="social-dot"></span>vkbtqm</li>
      <li><span class="social-dot"></span>Vandell Jewelry</li>
    </ul>
  </section>

</main>
</body>
</html>
```